Business Telephone Service Brochure

I need a brochure designed to help sell our VoIP service. The brochure needs to be clean, attention getting, professional and have 3 key areas of information (Key Features, Benefits & Service Plans). Here is an idea of what we are looking for https://www.artflockly.com/design/52930487. Need to also include how much the customer could save. See this for an example https://42mockups.com/postcard-flyer-design/contests/voip-sales-flyer-template-replicate-attached-358209. The Service Plan section needs to allow room for two types of plans. One plan includes the phone and has a 12, 24 and 36 month option. Each term (12,24,36) will have its own monthly cost per device. The second service option is no-commitment monthly with a single per month price per device. The included features section should allow for up to 16 features to be listed. The benefits should allow for 4-6 benefits to be listed. Also include room for Logo, business address, website, phone number and email.

Target Market(s)

Small to medium business with 1-100 employees.

Industry/Entity Type

Telecommunications

Font styles to use
Serif

Colors

Designer to choose colors to be used in the design.

Requirements
Must have
• Key Feature, Benefits and Service Plans (i.e. Pricing). Company logo, phone, email and website. Must have "Save up to x%!" and catch attention.
Nice to have
• Limited colors. I am not setting a hard limit, please take the liberty to do what you feel is needed. Just keep in mind we want it to be clean, professional and attention getting without being to flashy or obnoxious.
Should not have
• Nothing busy or distracting.

```html
<!DOCTYPE html>
<html lang="en">
<head>
<meta charset="utf-8">
<title>Novalink VoIP Flyer</title>
<link rel="stylesheet" href="https://fonts.googleapis.com/css2?family=Arimo:ital,wght@0,400;0,700;1,700&family=Anton&display=swap">
<style>
  :root {
    --canvas: #f1f1f1;
    --charcoal: #3b393a;
    --orange: #f47b20;
    --cyan: #2ec4f2;
    --navy: #233e7a;
    --green: #1f9a48;
    --blue: #1a78c2;
    --logo-ink: #2e2f7f;
    --white: #ffffff;
    --rule: #2c2a2b;
  }
  * { margin: 0; padding: 0; box-sizing: border-box; }
  html, body { width: 1200px; height: 893px; overflow: hidden; background: var(--canvas); }
  body { position: relative; font-family: "Arimo", Arial, sans-serif; color: var(--white); }

  .page { position: absolute; top: 106px; transform-origin: 0 0; transform: scale(0.8); overflow: hidden; background: var(--charcoal); }
  .page--front { left: 73px; width: 620px; height: 864px; }
  .page--back { left: 632px; width: 618px; height: 864px; }
  .page svg.backdrop { position: absolute; inset: 0; z-index: 0; }

  .logo-box { position: absolute; z-index: 2; left: 372px; top: 24px; width: 221px; height: 108px; background: var(--white); border: 2px solid #555; border-radius: 8px; text-align: center; }
  .logo-name { display: block; margin-top: 16px; font-size: 46px; font-weight: 700; color: var(--logo-ink); line-height: 1; }
  .logo-tagline { display: block; margin-top: 16px; font-size: 11.5px; color: #555; }

  .save { position: absolute; z-index: 3; left: 70px; top: 400px; transform: rotate(-14deg); transform-origin: 0 0; font-family: "Anton", Impact, sans-serif; color: var(--orange); line-height: 0.95;
    text-shadow: -2px -2px 0 var(--white), 2px -2px 0 var(--white), -2px 2px 0 var(--white), 2px 2px 0 var(--white), 0 -2px 0 var(--white), 0 2px 0 var(--white), -2px 0 0 var(--white), 2px 0 0 var(--white), 4px 5px 4px rgba(0,0,0,0.55); }
  .save-big { font-size: 84px; letter-spacing: 1px; }
  .save-small { font-size: 42px; margin-left: 18px; margin-top: -4px; }

  .plans { position: absolute; z-index: 2; left: 27px; top: 534px; width: 565px; border-collapse: collapse; }
  .plans th, .plans td { border: 1.5px solid var(--rule); }
  .plans th { background: var(--orange); height: 67px; font-size: 18px; font-weight: 400; line-height: 1.2; }
  .plans td { height: 95px; background: var(--blue); text-align: center; font-size: 18px; font-weight: 700; font-style: italic; }
  .plans td.plan-name { background: var(--green); text-align: left; padding-left: 12px; font-size: 14px; font-weight: 400; font-style: normal; line-height: 1.6; }
  .plans .star { color: var(--orange); }
  .plans .col-service { width: 172px; }
  .footnote { position: absolute; z-index: 2; left: 27px; top: 790px; width: 565px; height: 38px; border: 1px solid #222; padding: 4px 6px; font-size: 11px; line-height: 1.45; color: #eee; }

  .col-title { position: absolute; z-index: 2; top: 286px; font-size: 20px; font-weight: 700; }
  .bullets { position: absolute; z-index: 2; list-style: none; font-size: 14.5px; line-height: 21px; letter-spacing: 0.3px; }
  .bullets li { padding-left: 14px; position: relative; }
  .bullets li::before { content: "•"; position: absolute; left: 0; }
  .features-title, .features { left: 35px; }
  .features { top: 318px; width: 236px; }
  .benefits-title, .benefits { left: 350px; }
  .benefits { top: 318px; width: 240px; }
  .contact { position: absolute; z-index: 2; left: 340px; top: 786px; font-size: 11.5px; line-height: 16px; color: #eee; }
</style>
</head>
<body>

<section class="page page--front">
  <svg class="backdrop" width="620" height="864" viewBox="0 0 620 864">
    <defs>
      <linearGradient id="office" x1="0" y1="0" x2="1" y2="1">
        <stop offset="0" stop-color="#d9dde2"/>
        <stop offset="0.5" stop-color="#b9c0c8"/>
        <stop offset="1" stop-color="#6f7a86"/>
      </linearGradient>
    </defs>
    <polygon role="img" aria-label="Photo of a smiling call-centre agent wearing a headset in a bright office" fill="url(#office)" points="0,0 620,0 620,420 0,330"/>
    <polygon fill="var(--cyan)" points="0,307 432,460 432,507 0,357"/>
    <polygon fill="var(--navy)" points="200,347 620,450 620,478 230,362"/>
    <polygon fill="var(--orange)" points="130,350 620,470 620,532 60,375"/>
    <polygon fill="var(--green)" points="510,400 620,355 620,432"/>
  </svg>

  <div class="logo-box">
    <span class="logo-name">novalink</span>
    <span class="logo-tagline">Internet-Telephone-Security-Networking</span>
  </div>

  <div class="save">
    <div class="save-big">Save</div>
    <div class="save-small">up to 50%!</div>
  </div>

  <table class="plans">
    <tr>
      <th class="col-service">Service</th>
      <th>Monthly</th>
      <th>12 Month<br>Term</th>
      <th>24 Month<br>Term</th>
      <th>36 Month<br>Term</th>
    </tr>
    <tr>
      <td class="plan-name"><span class="star">*</span>Phone service only<br>(phone sold separately)</td>
      <td>$21.95</td><td></td><td></td><td></td>
    </tr>
    <tr>
      <td class="plan-name">Service + <span class="star">**</span>Vantel<br>V23 Phone</td>
      <td></td><td>$24.95</td><td>$22.95</td><td>$20.95</td>
    </tr>
  </table>
  <div class="footnote">
    *&nbsp; For monthly service you may purchase the Vantel V23 phone for $65 each, less taxes and shipping.<br>
    ** Vantel V23 phones are rented and due upon cancellation. Customer pays return shipping.
  </div>
</section>

<section class="page page--back">
  <svg class="backdrop" width="618" height="864" viewBox="0 0 618 864">
    <defs>
      <linearGradient id="tech" x1="0" y1="0" x2="1" y2="1">
        <stop offset="0" stop-color="#2b3446"/>
        <stop offset="0.6" stop-color="#3f6d8c"/>
        <stop offset="1" stop-color="#8fc3d6"/>
      </linearGradient>
      <linearGradient id="devices" x1="0" y1="0" x2="0" y2="1">
        <stop offset="0" stop-color="#6a6d72"/>
        <stop offset="1" stop-color="#1f2022"/>
      </linearGradient>
    </defs>
    <polygon fill="var(--orange)" points="0,232 277,322 277,839 0,747"/>
    <polygon fill="var(--blue)" points="340,310 618,300 618,729 340,624"/>
    <polygon role="img" aria-label="Photo of a businessman holding a tablet with glowing network graphics" fill="url(#tech)" points="0,0 618,0 618,322 277,322 0,232"/>
    <rect role="img" aria-label="Product photo of desk IP phones" fill="url(#devices)" x="345" y="632" width="250" height="105" rx="8"/>
  </svg>

  <h2 class="col-title features-title">Key Features</h2>
  <ul class="bullets features">
    <li>Unlimited local and long distance calling</li>
    <li>HD Voice</li>
    <li>Business SMS/Text Messaging</li>
    <li>Personal and Shared Voicemail Boxes</li>
    <li>Audio Conferencing</li>
    <li>Intercom</li>
    <li>Mobile App</li>
    <li>Auto Attendant/Interactive Voice Routing</li>
    <li>Free web or email fax</li>
    <li>Web admin portal</li>
    <li>Music On Hold - Customizable</li>
    <li>Simultaneous ring / follow-me</li>
    <li>Redundancy/Failover – Never miss a call</li>
  </ul>

  <h2 class="col-title benefits-title">Benefits</h2>
  <ul class="bullets benefits">
    <li>No expensive onsite telephone equipment</li>
    <li>Easily scale up or down and needs change</li>
    <li>Free telephone/email support</li>
    <li>Lower monthly cost</li>
    <li>Increase reliability</li>
    <li>Easy self-administration</li>
  </ul>

  <div class="contact">
    phone number:000-000-000<br>
    email:<br>
    website:
  </div>
</section>

</body>
</html>
```